Main Webpage Graphic depicting what our business is all about

Our website is ferngavelhouse.net We are developing a new website and need graphics for the main page background main image. we are an online auction so I was thinking The background would be water with ripples, then have a laptop open on the side, then have examples of items we sell, our logo, gavels, bursting out of the the screen on the laptop and spewing across the screen.

Font styles to use
Other font styles liked:

Colors
85cae6
33a6d7
0293ce
0355a3
3276b5
85abd2

```html
<!DOCTYPE html>
<html lang="en">
<head>
<meta charset="utf-8">
<title>Ferngavelhouse – Local Online Auction</title>
<link href="https://fonts.googleapis.com/css2?family=Montserrat:wght@300;400;500;600;700&family=Open+Sans:wght@400&display=swap" rel="stylesheet">
<style>
  :root {
    --brand-warm-start: #e05a56;
    --brand-warm-end: #f58a3e;
    --button-start: #e8501f;
    --button-end: #f07d48;
    --water-deep: #1f3f7a;
    --water-mid: #2f559a;
    --water-light: #4a6fae;
    --ink: #333333;
    --nav-ink: #3d3d3d;
    --logo-blue: #0355a3;
    --logo-dot: #0293ce;
    --white: #ffffff;
    --field-bg: #f8f6f5;
    --field-line: #b9b9b9;
    --orange: #ee6a2c;
  }
  * { box-sizing: border-box; margin: 0; padding: 0; }
  html, body { width: 1200px; height: 857px; overflow: hidden; }
  body { position: relative; font-family: "Montserrat", sans-serif; background: var(--white); color: var(--ink); }

  .masthead {
    position: absolute; left: 0; top: 0; width: 1200px; height: 116px;
    background: linear-gradient(90deg, var(--brand-warm-start), var(--brand-warm-end));
  }
  .utility-bar { position: absolute; left: 0; top: 0; width: 1200px; height: 40px; border-bottom: 1px solid rgba(255,255,255,0.75); }
  .social-links { position: absolute; left: 120px; top: 8px; display: flex; gap: 10.5px; list-style: none; }
  .social-links li { width: 22px; height: 22px; background: var(--white); border-radius: 3px; }
  .utility-phone { position: absolute; right: 120px; top: 6px; font-family: "Open Sans", sans-serif; font-size: 22px; color: var(--white); }

  .brand { position: absolute; left: 128px; top: 72px; display: flex; align-items: center; gap: 10px; }
  .brand-dot { width: 24px; height: 24px; border-radius: 50%; background: var(--logo-dot); }
  .brand-name { font-size: 20px; font-weight: 600; color: var(--logo-blue); letter-spacing: 0.2px; }

  .main-nav { position: absolute; right: 120px; top: 90px; display: flex; gap: 32px; list-style: none; }
  .main-nav li { font-size: 15px; color: var(--nav-ink); font-weight: 400; }
  .main-nav li.is-current { font-weight: 600; }

  .hero { position: absolute; left: 0; top: 116px; width: 1200px; height: 475px; }
  .hero-backdrop {
    position: absolute; inset: 0;
    background: radial-gradient(ellipse at 30% 40%, var(--water-light), transparent 60%),
                linear-gradient(180deg, var(--water-mid), var(--water-deep));
  }
  .hero-title { position: absolute; left: 118px; top: 126px; font-size: 33px; font-weight: 700; letter-spacing: 9px; color: rgba(190,205,235,0.75); }
  .hero-subtitle { position: absolute; left: 118px; top: 162px; font-size: 36px; font-weight: 300; color: rgba(190,205,235,0.7); }
  .cta-button {
    position: absolute; display: flex; align-items: center; justify-content: center; text-align: center;
    background: linear-gradient(90deg, var(--button-start), var(--button-end));
    color: var(--white); font-weight: 700; font-size: 12.5px; letter-spacing: 0.8px; line-height: 1.15;
    border-radius: 3px;
  }
  .cta-enter { left: 120px; top: 216px; width: 167px; height: 49px; }
  .cta-upcoming { left: 309px; top: 216px; width: 167px; height: 49px; }

  .showcase-frame { position: absolute; left: 619px; top: 71px; width: 461px; height: 289px; background: rgba(200,210,230,0.45); border-radius: 6px; }
  .showcase-stand { position: absolute; left: 782px; top: 360px; }
  .showcase-screen { position: absolute; left: 634px; top: 86px; width: 432px; height: 260px; background: var(--white); }
  .lot-photo { position: absolute; left: 31px; top: 33px; width: 195px; height: 175px; background: radial-gradient(circle at 50% 50%, #3a3a3a 0 38%, #e8762a 39% 46%, #f2f2f2 60%); }
  .slider-arrow { position: absolute; top: 121px; }
  .slider-prev { left: 8px; }
  .slider-next { left: 406px; }
  .lot-details { position: absolute; left: 243px; top: 46px; width: 160px; }
  .lot-number { font-size: 19px; font-weight: 700; color: var(--ink); margin-bottom: 4px; }
  .lot-description { font-size: 14.5px; line-height: 17.4px; letter-spacing: 0.4px; color: var(--ink); }
  .bid-button { left: 240px; top: 184px; width: 144px; height: 35px; font-size: 12.5px; }

  .newsletter { position: absolute; left: 0; top: 591px; width: 1200px; height: 150px; }
  .newsletter-title { position: absolute; top: 25px; width: 100%; text-align: center; font-size: 21px; font-weight: 400; letter-spacing: 2.3px; color: var(--ink); }
  .newsletter-field {
    position: absolute; top: 82px; width: 242px; height: 28px; background: var(--field-bg);
    border: 1px dashed var(--field-line); border-radius: 3px;
    font-family: "Montserrat", sans-serif; font-size: 12.5px; letter-spacing: 1.5px; color: #555; padding-left: 10px;
  }
  .field-one { left: 174px; }
  .field-two { left: 435px; }
  .field-three { left: 694px; }
  .newsletter-submit {
    position: absolute; left: 953px; top: 80px; width: 73px; height: 28px; background: var(--white);
    border: 1px dashed var(--field-line); border-radius: 2px;
    font-family: "Montserrat", sans-serif; font-size: 12.5px; letter-spacing: 1.5px; color: #555;
  }

  .site-footer {
    position: absolute; left: 0; top: 741px; width: 1200px; height: 116px;
    background: linear-gradient(90deg, var(--brand-warm-start), var(--brand-warm-end));
  }
  .footer-line { position: absolute; top: 50px; width: 100%; text-align: center; font-size: 12.5px; letter-spacing: 1.3px; color: var(--white); word-spacing: 1px; }
</style>
</head>
<body>
  <header class="masthead">
    <div class="utility-bar">
      <ul class="social-links" aria-label="Social links">
        <li></li><li></li><li></li><li></li><li></li>
      </ul>
      <div class="utility-phone">810-555-0172</div>
    </div>
    <div class="brand">
      <span class="brand-dot"></span>
      <span class="brand-name">FERNGAVELHOUSE</span>
    </div>
    <ul class="main-nav">
      <li class="is-current">HOME</li>
      <li>BUY</li>
      <li>SERVICES</li>
      <li>CONTACTS</li>
      <li>NEWS</li>
      <li>FAQ</li>
      <li>SHIPPING</li>
    </ul>
  </header>

  <section class="hero">
    <div class="hero-backdrop" role="img" aria-label="Rippled deep blue water surface"></div>
    <h1 class="hero-title">FERNGAVELHOUSE</h1>
    <p class="hero-subtitle">Local Online Auction</p>
    <div class="cta-button cta-enter">ENTER AUCTION</div>
    <div class="cta-button cta-upcoming">ALL UPCOMING<br>AUCTION</div>

    <div class="showcase-frame"></div>
    <svg class="showcase-stand" width="118" height="36" viewBox="0 0 118 36" aria-hidden="true">
      <path d="M16 0 H102 V6 Q104 24 118 36 H0 Q14 24 16 6 Z" fill="rgba(200,210,230,0.45)"/>
    </svg>
    <div class="showcase-screen">
      <div class="lot-photo" role="img" aria-label="Black and orange benchtop thickness planer"></div>
      <svg class="slider-arrow slider-prev" width="19" height="19" viewBox="0 0 19 19" aria-label="Previous lot">
        <circle cx="9.5" cy="9.5" r="8.3" fill="none" stroke="var(--orange)" stroke-width="1.8"/>
        <path d="M14 9.5 H6 M9 6 L5.5 9.5 L9 13" fill="none" stroke="var(--orange)" stroke-width="2" stroke-linecap="round" stroke-linejoin="round"/>
      </svg>
      <svg class="slider-arrow slider-next" width="19" height="19" viewBox="0 0 19 19" aria-label="Next lot">
        <circle cx="9.5" cy="9.5" r="8.3" fill="none" stroke="var(--orange)" stroke-width="1.8"/>
        <path d="M5 9.5 H13 M10 6 L13.5 9.5 L10 13" fill="none" stroke="var(--orange)" stroke-width="2" stroke-linecap="round" stroke-linejoin="round"/>
      </svg>
      <div class="lot-details">
        <h2 class="lot-number">Lot 49-314340</h2>
        <p class="lot-description">Kestrel 15 amp 12.5" Corded Thickness Planer, 18000 rpm, depth adjustment, Model #: 4120. Unused</p>
      </div>
      <div class="cta-button bid-button">PLACE BID</div>
    </div>
  </section>

  <section class="newsletter">
    <h2 class="newsletter-title">Email Updates And Newsletter</h2>
    <input class="newsletter-field field-one" type="text" placeholder="name">
    <input class="newsletter-field field-two" type="text" placeholder="name">
    <input class="newsletter-field field-three" type="text" placeholder="name">
    <button class="newsletter-submit" type="button">submit</button>
  </section>

  <footer class="site-footer">
    <p class="footer-line">Ferngavelhouse.net Online Auctions 2016&nbsp;&nbsp; 48 Harbor Mill Rd&nbsp; Lakeport, MI 48049&nbsp; 810-555-0172&nbsp; info@ferngavelhouse.net</p>
  </footer>
</body>
</html>
```